New (old) Business Card Design Project

I would like to purchase a customized version of a design you have previously submitted - https://www.artmarketly.example/design/7305126

I like the card above, and would like to use the same design, jus with my business name, HARLOWAY ASSET ADVISORS. I like the colors in the card above, as well as the font. The other side will have my name, company name, address, phone, email, website, plus disclosure text I will provide.

Target Market(s)

wealthy families

Industry/Entity Type

Financial Services

Contact Information for Business Card

logo on one side, on other my name, company, address, phone, email, website, disclosure language I will provide.

Colors

Designer to choose colors to be used in the design.

Requirements
Must have
• colors: Deep blue and white
Nice to have
• Please see the items I have uploaded, below.
Should not have
• Cheap, tacky look.

```html
<!DOCTYPE html>
<html lang="en">
<head>
<meta charset="utf-8">
<title>Harloway Asset Advisors — Business Card</title>
<link rel="stylesheet" href="https://fonts.googleapis.com/css2?family=Cormorant+Garamond:wght@500&family=Montserrat:wght@400;600&display=swap">
<style>
  :root {
    --navy: #0b2461;
    --navy-text: #12296e;
    --ink-grey: #555a63;
    --paper: #f4f4f3;
    --stage: #f3f2f0;
    --rule: #8c98b8;
    --white: #ffffff;
  }
  * { box-sizing: border-box; margin: 0; padding: 0; }
  html, body {
    width: 1200px; height: 800px; overflow: hidden;
    background: var(--stage);
  }
  .sheet {
    position: relative; width: 1200px; height: 800px;
    display: flex; align-items: center; justify-content: center; gap: 60px;
  }
  .card {
    position: relative; width: 520px; height: 300px;
    box-shadow: 0 2px 6px rgba(0,0,0,0.08);
  }
  .card--front { background: var(--paper); }
  .card--back { background: var(--navy); }

  .brand {
    font-family: "Cormorant Garamond", Georgia, serif;
    font-weight: 500;
    text-transform: uppercase;
    letter-spacing: 0.14em;
    white-space: nowrap;
  }
  .card--front .brand {
    position: absolute; left: 34px; top: 92px;
    font-size: 17px; line-height: 1.3; color: var(--navy-text);
  }
  .brand__line { display: block; }
  .card--back .brand {
    position: absolute; left: 0; right: 0; top: 132px;
    text-align: center; font-size: 26px; color: var(--white);
  }

  .divider {
    position: absolute; left: 270px; top: 146px;
    width: 1px; height: 124px; background: var(--rule);
  }
  .contact {
    position: absolute; left: 286px; top: 150px;
    font-family: "Montserrat", Arial, sans-serif;
    color: var(--ink-grey);
    white-space: nowrap;
  }
  .contact__name {
    font-weight: 600; font-size: 19px; letter-spacing: 0.03em;
    color: var(--navy-text); line-height: 1.1;
  }
  .contact__title {
    font-size: 11px; letter-spacing: 0.06em; text-transform: uppercase;
    margin: 3px 0 8px;
  }
  .contact__line { font-size: 11px; line-height: 1.55; }
  .contact__web { font-size: 11px; line-height: 1.55; color: var(--navy-text); }
</style>
</head>
<body>
  <main class="sheet">
    <section class="card card--front" aria-label="Card front">
      <p class="brand">
        <span class="brand__line">Harloway</span>
        <span class="brand__line">Asset Advisors</span>
      </p>
      <div class="divider"></div>
      <div class="contact">
        <p class="contact__name">DANIEL REEVE</p>
        <p class="contact__title">Managing Director</p>
        <p class="contact__line">TEL: XXX XXX XXXX</p>
        <p class="contact__line">FAX: XXX XXX XXXX</p>
        <p class="contact__line">EMAIL: daniel@harloway.example</p>
        <p class="contact__web">www.harloway.example</p>
      </div>
    </section>
    <section class="card card--back" aria-label="Card back">
      <p class="brand">Harloway Asset Advisors</p>
    </section>
  </main>
</body>
</html>
```